Ferncrest Dental, LLC business card project

Business card to be designed with current logo.
Dental office- please keep design of card that looks clean and professional.
Please include the following info:
Ferncrest Dental, LLC
Dr. Lorna Pettigrew
2871 Marlowe Street
Bethlehem, PA 18093
610-555-0193
ferncrestdental.office@examplemail.test
Hello everyone-
Reason: Just got back from overseas- will look at all designs and provide feedback. Thank you!
Reason: Polling my friends for the final selection-
thank you to all those that participated- so many talented designers!

```html
<!DOCTYPE html>
<html lang="en">
<head>
<meta charset="utf-8">
<title>Ferncrest Dental, LLC – Business Cards</title>
<link href="https://fonts.googleapis.com/css2?family=Arimo:ital,wght@0,400;0,700;1,700&display=swap" rel="stylesheet">
<style>
  :root {
    --page: #ffffff;
    --card: #ffffff;
    --edge: #2b2b2b;
    --green: #8db33a;
    --green-soft: #c9dca0;
    --green-pale: #eef4e0;
    --grey-pale: #eef0ec;
    --ink: #1f1f1f;
    --blue: #1d2a86;
  }
  * { box-sizing: border-box; margin: 0; padding: 0; }
  html, body { width: 1200px; height: 900px; overflow: hidden; background: var(--page); }
  body { position: relative; font-family: "Arimo", Arial, sans-serif; color: var(--ink); }

  .card {
    position: absolute; width: 384px; height: 176px;
    background: var(--card); border: 1px solid var(--edge); overflow: hidden;
  }
  .front { left: 187px; }
  .back { left: 629px; }
  .row-1 { top: 108px; }
  .row-2 { top: 322px; }
  .row-3 { top: 552px; height: 190px; }

  .pattern {
    position: absolute; left: 0; right: 0;
    background: linear-gradient(135deg, var(--green-pale), var(--grey-pale) 50%, var(--green-pale));
  }
  .pattern.full { top: 0; bottom: 0; }
  .pattern.top { top: 0; height: 52px; }
  .pattern.bottom { bottom: 0; height: 40px; }

  .brand {
    position: absolute; display: flex; align-items: center; gap: 6px;
    font-weight: 700; color: var(--green); white-space: nowrap;
  }
  .brand-mark { width: 9px; height: 9px; background: var(--green); }
  .brand.center { left: 0; right: 0; justify-content: center; font-size: 22px; }
  .row-1 .brand.center, .row-2 .brand.center { top: 68px; }
  .row-3 .brand.center { top: 60px; font-size: 18px; }
  .brand.corner { left: 16px; top: 30px; font-size: 15px; }

  .rule-top { position: absolute; left: 0; right: 0; top: 58px; height: 2px; background: var(--green-soft); }
  .band-bottom { position: absolute; left: 0; right: 0; bottom: 0; height: 9px; background: var(--green-soft); }

  .header-name { position: absolute; left: 150px; top: 30px; font-size: 15px; font-weight: 700; color: var(--green); }

  .details {
    position: absolute; right: 16px; text-align: right;
    font-size: 10px; line-height: 13px; font-weight: 700;
  }
  .details .company { font-size: 12px; margin-bottom: 10px; }
  .details .doctor { font-size: 15px; color: var(--green); margin-bottom: 12px; }
  .email { color: var(--blue); font-style: italic; font-weight: 700; }
  .row-1 .details { top: 76px; }
  .row-2 .details { top: 68px; }

  .tooth {
    position: absolute; left: 118px; top: 46px; width: 60px; height: 82px;
    border-radius: 40% 40% 45% 45%;
    background: radial-gradient(circle at 50% 40%, #fbfbfb, #f0f0f0);
  }

  .centered {
    position: absolute; left: 0; right: 0; text-align: center;
    font-size: 10px; line-height: 12px; font-weight: 700;
  }
  .centered .doctor { font-size: 14px; margin-bottom: 10px; }
  .row-3.front .centered { top: 92px; }

  .appointment { position: absolute; inset: 0; padding: 10px 18px; text-align: center; font-size: 9px; line-height: 11px; font-weight: 700; }
  .appointment .lead { border-bottom: 1px solid var(--ink); width: 70%; margin: 0 auto 4px; padding-bottom: 2px; font-weight: 400; }
  .appointment .doctor { font-size: 14px; line-height: 17px; margin-bottom: 4px; }
  .slots { width: 100%; margin: 12px 0 6px; border-collapse: collapse; }
  .slots td { text-align: left; font-weight: 400; padding-top: 5px; }
  .slots .line { border-bottom: 1px solid var(--ink); width: 38%; }
  .slots .label { width: 12%; padding-left: 4px; }
  .note { font-size: 9px; }
</style>
</head>
<body>

  <!-- Version 1 -->
  <section class="card front row-1">
    <div class="pattern full" role="img" aria-label="Soft repeated brand pattern in pale green and grey"></div>
    <div class="brand center"><span class="brand-mark"></span>Ferncrest Dental, LLC</div>
  </section>
  <section class="card back row-1">
    <div class="brand corner"><span class="brand-mark"></span></div>
    <div class="header-name" style="left:34px">Dr. Lorna Pettigrew</div>
    <div class="rule-top"></div>
    <div class="details">
      <div class="company">Ferncrest Dental, LLC</div>
      <div>2871 Marlowe Street</div>
      <div>Bethlehem, PA 18093</div>
      <div>610-555-0193</div>
      <div class="email">ferncrestdental.office@examplemail.test</div>
    </div>
    <div class="band-bottom"></div>
  </section>

  <!-- Version 2 -->
  <section class="card front row-2">
    <div class="pattern full" role="img" aria-label="Soft repeated brand pattern in pale green and grey"></div>
    <div class="brand center"><span class="brand-mark"></span>Ferncrest Dental, LLC</div>
  </section>
  <section class="card back row-2">
    <div class="brand corner" style="top:22px"><span class="brand-mark"></span>Ferncrest Dental, LLC</div>
    <div class="tooth" role="img" aria-label="Faint tooth illustration"></div>
    <div class="details">
      <div class="doctor">Dr. Lorna Pettigrew</div>
      <div>2871 Marlowe Street</div>
      <div>Bethlehem, PA 18093</div>
      <div>610-555-0193</div>
      <div class="email">ferncrestdental.office@examplemail.test</div>
    </div>
  </section>

  <!-- Version 3 -->
  <section class="card front row-3">
    <div class="pattern top" role="img" aria-label="Soft repeated brand pattern in pale green and grey"></div>
    <div class="brand center"><span class="brand-mark"></span>Ferncrest Dental, LLC</div>
    <div class="centered">
      <div class="doctor">Dr. Lorna Pettigrew</div>
      <div>2871 Marlowe Street</div>
      <div>Bethlehem, PA 18093</div>
      <div>610-555-0193</div>
      <div class="email">ferncrestdental.office@examplemail.test</div>
    </div>
    <div class="pattern bottom" role="img" aria-label="Soft repeated brand pattern in pale green and grey"></div>
  </section>
  <section class="card back row-3">
    <div class="appointment">
      <div class="lead">has the following appointment with</div>
      <div class="doctor">Dr. Lorna Pettigrew</div>
      <div>2871 Marlowe Street</div>
      <div>Bethlehem, PA 18093</div>
      <div>610-555-0193</div>
      <div class="email">ferncrestdental.office@examplemail.test</div>
      <table class="slots">
        <tr><td class="line">Date</td><td class="label"></td><td class="line">Time</td></tr>
        <tr><td class="line">Date</td><td class="label"></td><td class="line">Time</td></tr>
        <tr><td class="line">Date</td><td class="label"></td><td class="line">Time</td></tr>
      </table>
      <div class="note">Please phone 610-555-0193 if unable to keep appointment</div>
    </div>
  </section>

</body>
</html>
```